Law Firm Web Design Project

I need a website design for my law firm. I have attached to this description the URL of a website I liked with a description of the elements of that website that appeal to me.

I am also attaching my law firm's logo, so you can review that design when you create the website design.

Reference Site: www.harborfamilycounselpros.com

What we like about this site:
• The different layers
• Subtle designs, textures, curves
• 3 dimensional
• Floating effect
• Simple logo that stands out (we are providing logo)
• Prominent phone number
• Location of Areas of Practice
oDivorce, Legal Separation, Paternity, Spousal Maintenance, Child Custody, Child Support, Protective Orders, Community Property, Business Evaluations
• The limited amount of links across the top
o Home, Meet Our Attorney, FAQ, Contact Us
• Request A Consultation click through
• Right side bar with the moving icons
• Badges

Other Tips:
• We don’t want the website to be dark. The logo can standout and the website can have its own colors and flow.
• We would like there to be a “call to action” or way to get in touch on every page and every page view
• We would like a place for credit card icons at the bottom of the page
• Strong, yet elegant
• Finally, just use the website provided as a guide. Explore different colors, textures, shapes, shadows etc.
Updates

I would prefer the website have colors that are complementary to my logo and that are strong and elegant.  I like black, gold, amber, and tan colors.  Black should be used sparingly as an accent only, since I don't want the website to be too dark.

Please review the website I provided as an example in my project description.  I really like the three dimensional aspects of that website (web page floating on top of a background and the logo in the upper left floating on top of the web page).  I also like the use of "swirling" on the background and the webpage.  I hope this additional information is helpful.

Requirements
Must have
• I need a place to insert "client testimonials", a place to insert four logos of awards the law firm has received, a place for people to fill out a form to contact the law firm via email, and a place for people to click to review articles I have written.

```html
<!DOCTYPE html>
<html lang="en">
<head>
<meta charset="utf-8">
<title>Halvorsen Law</title>
<link href="https://fonts.googleapis.com/css2?family=Arimo:wght@400;700&family=Cinzel:wght@400;600&family=Lora:ital,wght@0,400;1,400&family=Ubuntu:wght@300;400;500;700&display=swap" rel="stylesheet">
<style>
:root{
  --gold:#d9a21c;
  --gold-light:#ecbc32;
  --gold-deep:#b07e0c;
  --brown:#5e3d05;
  --brown-dark:#3f2903;
  --cream:#f3e2bc;
  --cream-light:#f7efdc;
  --ink:#1f1a12;
  --swoosh:#2b2b2b;
  --white:#ffffff;
}
*{margin:0;padding:0;box-sizing:border-box}
html,body{width:990px;height:1200px;overflow:hidden}
body{background:radial-gradient(ellipse at 50% 40%,#e9b627 0%,#c08a10 55%,#8a5e06 100%);font-family:Arimo,Arial,sans-serif;position:relative}
.page{position:absolute;left:66px;top:0;width:858px;height:1200px;background:var(--cream);box-shadow:0 0 18px rgba(60,35,0,.45)}
.abs{position:absolute}

/* header */
.header{left:0;top:0;width:858px;height:106px;background:var(--cream-light)}
.brand{left:30px;top:22px;display:flex;align-items:center;gap:14px}
.brand-mark{width:48px;height:48px;background:var(--ink)}
.brand-name{font-family:Lora,serif;font-size:32px;color:#a98a3a;letter-spacing:1px}
.help-figure{left:590px;top:18px;width:52px;height:56px;border-radius:6px;background:linear-gradient(160deg,#f0f0f0,#c9a22a)}
.help-label{left:656px;top:22px;font-family:Ubuntu,sans-serif;font-weight:700;font-size:13px;letter-spacing:1px;color:var(--ink)}
.help-phone{left:647px;top:40px;font-family:Ubuntu,sans-serif;font-weight:700;font-size:26px;color:#c8930f;letter-spacing:1px}

/* nav */
.nav{left:0;top:106px;width:858px;height:34px;background:linear-gradient(#f1c445,#d9a21c);border-top-right-radius:22px}
.nav a{position:absolute;top:0;height:34px;line-height:34px;font-family:Ubuntu,sans-serif;font-weight:500;font-size:11px;color:var(--white);text-decoration:none}
.nav .active{left:0;width:72px;background:var(--brown);border-top-left-radius:18px;text-align:center}
.social{position:absolute;top:8px;height:18px;padding:0 4px;border-radius:3px;font-family:Ubuntu,sans-serif;font-size:9px;line-height:18px;color:var(--white)}

/* hero */
.hero{left:0;top:142px;width:858px;height:380px}
.tagline{left:593px;top:216px;font-family:Cinzel,serif;font-size:30px;line-height:46px}
.tagline .q{color:#b58a1d;display:block}
.tagline .a{color:var(--ink);display:block}

/* columns */
.col-left{left:0;top:380px;width:201px;height:758px;background:var(--gold)}
.col-right{left:648px;top:370px;width:210px;height:768px;background:var(--gold)}

.practice-title{left:13px;top:506px;font-family:Ubuntu,sans-serif;font-weight:700;font-size:20px;color:var(--ink);letter-spacing:.5px}
.practice-list{left:14px;top:550px;list-style:none}
.practice-list li{height:27.5px;display:flex;align-items:center;gap:12px;font-family:Ubuntu,sans-serif;font-weight:500;font-size:10.5px;color:var(--white);letter-spacing:.3px}
.btn{display:inline-block;background:linear-gradient(#3a3a3a,#151515);border:1px solid #fff;color:var(--white);font-family:Arimo,sans-serif;font-size:12px;text-align:center}
.practice-more{left:14px;top:809px;width:67px;height:23px;line-height:21px}
.awards-title{left:14px;top:860px;display:flex;align-items:center;gap:10px;font-family:Ubuntu,sans-serif;font-weight:700;font-size:20px;color:var(--ink)}
.medal{width:26px;height:30px}
.badge{background:#f4f1ea;border:1px solid #e6dcc0}

/* middle */
.section-title{font-family:Ubuntu,sans-serif;font-weight:700;font-size:28px;color:#e0a522;text-shadow:1px 1px 0 #7a5410,2px 2px 3px rgba(0,0,0,.3)}
.icon-box{width:40px;height:40px;border-radius:4px}
.rule{left:213px;top:568px;width:422px;height:2px;background:var(--gold-deep)}
.article{left:217px;width:422px;font-size:10.5px;line-height:17px;color:#333;letter-spacing:.2px;padding-left:12px}
.article::before{content:"";position:absolute;left:0;top:6px;border-left:4px solid #555;border-top:3px solid transparent;border-bottom:3px solid transparent}
.view-link{left:580px;top:700px;font-size:10px;font-weight:700;color:#333}
.view-link span{color:var(--gold-deep)}
.testimonial-bar{left:204px;top:725px;width:431px;height:31px;background:linear-gradient(#6d4808,var(--brown))}
.testimonial-title{left:269px;top:729px;font-family:Ubuntu,sans-serif;font-weight:300;font-size:19px;color:var(--white);letter-spacing:1px}
.testimonial-more{left:556px;top:729px;width:67px;height:23px;line-height:21px}
.note-icon{left:214px;top:712px;width:44px;height:48px;background:#fbfaf5;border:1px solid #ddd;transform:rotate(-8deg);box-shadow:1px 2px 4px rgba(0,0,0,.3)}
.quote{left:217px;width:424px;font-family:Lora,serif;font-style:italic;font-size:14px;line-height:21px;color:#3a3020;text-align:justify;padding-left:16px}
.quote::before{content:"\201C";position:absolute;left:-2px;top:-6px;font-family:Lora,serif;font-size:30px;font-style:normal;color:var(--gold)}
.contact-intro{left:209px;top:996px;width:436px;font-size:10.5px;line-height:15px;color:#222;letter-spacing:.2px}
.field-label{font-size:12px;color:#222}
.field{background:var(--gold);height:19px}
.submit{left:541px;top:1105px;width:66px;height:22px;line-height:20px}

/* right sidebar */
.side-title{left:664px;font-family:Ubuntu,sans-serif;font-weight:300;font-size:19px;color:var(--ink);letter-spacing:.5px}
.side-text{left:718px;width:140px;font-family:Ubuntu,sans-serif;font-weight:500;font-size:10.5px;line-height:16.4px;color:var(--white);letter-spacing:.2px}
.side-icon{left:660px;width:50px;height:50px}

/* footer */
.footer{left:0;top:1138px;width:858px;height:62px;background:linear-gradient(#6b4806,#4a3104)}
.footer-brand{left:50px;top:1153px;display:flex;align-items:center;gap:8px;font-family:Lora,serif;font-size:13px;color:var(--gold-light)}
.footer-brand i{display:block;width:30px;height:30px;background:var(--ink)}
.footer-links{left:217px;top:1155px;width:400px;text-align:center;font-size:11px;color:var(--white);word-spacing:1px}
.footer-links span{margin:0 8px}
.copyright{left:217px;top:1177px;width:400px;text-align:center;font-size:11px;color:var(--white)}
.pay{height:22px;padding:0 5px;border-radius:3px;background:#f4f1ea;font-family:Arimo,sans-serif;font-weight:700;font-size:9px;line-height:22px;color:#1c3b7a;text-align:center}
.seal{height:18px;line-height:18px;font-size:8px}
</style>
</head>
<body>
<div class="page">

  <header class="header abs">
    <div class="brand abs"><span class="brand-mark"></span><span class="brand-name">Halvorsen Law</span></div>
    <div class="help-figure abs" role="img" aria-label="Illustration of a support agent with headset"></div>
    <div class="help-label abs">can we help you??</div>
    <div class="help-phone abs">02 5550 1842</div>
  </header>

  <nav class="nav abs">
    <a class="active" href="#">Home</a>
    <a href="#" style="left:95px">Meet Our Attorneys</a>
    <a href="#" style="left:237px">FAQ’s</a>
    <a href="#" style="left:307px">Contact Us</a>
    <span class="social" style="left:696px;background:#e8741b">Feed</span>
    <span class="social" style="left:729px;background:#3aa7d8">Chirp</span>
    <span class="social" style="left:760px;background:#3b5998">Facepage</span>
    <span class="social" style="left:810px;background:#1aa3e0">Callnet</span>
  </nav>

  <div class="col-left abs"></div>
  <div class="col-right abs"></div>

  <svg class="hero abs" viewBox="0 0 858 380" width="858" height="380">
    <defs>
      <linearGradient id="heroPhoto" x1="0" y1="0" x2="1" y2="0">
        <stop offset="0" stop-color="#b9a47a"/>
        <stop offset=".35" stop-color="#a55a3a"/>
        <stop offset=".6" stop-color="#8c93a3"/>
        <stop offset="1" stop-color="#efe6d2"/>
      </linearGradient>
    </defs>
    <path role="img" aria-label="Photograph of a troubled couple sitting apart outdoors" d="M0 0H858V234C700 242 520 322 310 330C170 334 70 306 0 282Z" fill="url(#heroPhoto)"/>
    <path d="M0 282C70 306 170 334 310 330C520 322 700 242 858 234V248C700 256 520 336 310 346C160 352 60 326 0 300Z" fill="var(--swoosh)"/>
  </svg>
  <div class="tagline abs"><span class="q">Problems ?</span><span class="a">Pick Quinlan</span></div>

  <!-- left column -->
  <h2 class="practice-title abs">Areas Of Practice</h2>
  <ul class="practice-list abs">
    <li><svg width="18" height="18" viewBox="0 0 18 18"><rect x="1" y="4" width="12" height="12" fill="none" stroke="#111" stroke-width="2"/><path d="M4 9l4 5L17 1" fill="none" stroke="#111" stroke-width="3"/></svg>Divorce</li>
    <li><svg width="18" height="18" viewBox="0 0 18 18"><rect x="1" y="4" width="12" height="12" fill="none" stroke="#111" stroke-width="2"/><path d="M4 9l4 5L17 1" fill="none" stroke="#111" stroke-width="3"/></svg>Legal Sepration</li>
    <li><svg width="18" height="18" viewBox="0 0 18 18"><rect x="1" y="4" width="12" height="12" fill="none" stroke="#111" stroke-width="2"/><path d="M4 9l4 5L17 1" fill="none" stroke="#111" stroke-width="3"/></svg>Paternity</li>
    <li><svg width="18" height="18" viewBox="0 0 18 18"><rect x="1" y="4" width="12" height="12" fill="none" stroke="#111" stroke-width="2"/><path d="M4 9l4 5L17 1" fill="none" stroke="#111" stroke-width="3"/></svg>Spousal Maintenance</li>
    <li><svg width="18" height="18" viewBox="0 0 18 18"><rect x="1" y="4" width="12" height="12" fill="none" stroke="#111" stroke-width="2"/><path d="M4 9l4 5L17 1" fill="none" stroke="#111" stroke-width="3"/></svg>child Custody</li>
    <li><svg width="18" height="18" viewBox="0 0 18 18"><rect x="1" y="4" width="12" height="12" fill="none" stroke="#111" stroke-width="2"/><path d="M4 9l4 5L17 1" fill="none" stroke="#111" stroke-width="3"/></svg>Child Support</li>
    <li><svg width="18" height="18" viewBox="0 0 18 18"><rect x="1" y="4" width="12" height="12" fill="none" stroke="#111" stroke-width="2"/><path d="M4 9l4 5L17 1" fill="none" stroke="#111" stroke-width="3"/></svg>Protective Orders</li>
    <li><svg width="18" height="18" viewBox="0 0 18 18"><rect x="1" y="4" width="12" height="12" fill="none" stroke="#111" stroke-width="2"/><path d="M4 9l4 5L17 1" fill="none" stroke="#111" stroke-width="3"/></svg>Community Property Business</li>
    <li><svg width="18" height="18" viewBox="0 0 18 18"><rect x="1" y="4" width="12" height="12" fill="none" stroke="#111" stroke-width="2"/><path d="M4 9l4 5L17 1" fill="none" stroke="#111" stroke-width="3"/></svg>Evaluations</li>
  </ul>
  <a class="btn practice-more abs">View All</a>

  <h2 class="awards-title abs"><svg class="medal" viewBox="0 0 26 30"><path d="M6 16L2 28l5-2 3 4 3-10M20 16l4 12-5-2-3 4-3-10" fill="#b8332a"/><circle cx="13" cy="11" r="10" fill="#e0b040" stroke="#9a6d12" stroke-width="2"/></svg>Awards</h2>
  <div class="badge abs" style="left:8px;top:919px;width:186px;height:78px"></div>
  <div class="badge abs" style="left:6px;top:1023px;width:55px;height:75px"></div>
  <div class="badge abs" style="left:67px;top:1023px;width:125px;height:75px"></div>

  <!-- middle column -->
  <div class="icon-box abs" role="img" aria-label="Illustration of a notepad and pen" style="left:214px;top:516px;background:linear-gradient(#fafafa,#c9c9c9)"></div>
  <h2 class="section-title abs" style="left:264px;top:517px">Latest Articles</h2>
  <div class="rule abs"></div>
  <p class="article abs" style="top:585px">Aenean ac diam eu erat suscipit dapibus in ac neque. Curabitur non nisi ut lorem acc nec in odio. Praesent hendrerit, lacus at eleifend commodo, massa sapien accumsan tudin diam mauris at arcu.</p>
  <p class="article abs" style="top:645px">Aenean ac diam eu erat suscipit dapibus in ac neque. Curabitur non nisi ut lorem acc nec in odio. Praesent hendrerit, lacus at eleifend commodo, massa sapien accumsan tudin diam mauris at arcu.</p>
  <div class="view-link abs">View All [<span>+</span>]</div>

  <div class="testimonial-bar abs"></div>
  <div class="note-icon abs" role="img" aria-label="Illustration of a handwritten testimonial note"></div>
  <div class="testimonial-title abs">Recent Testimonial</div>
  <a class="btn testimonial-more abs">View All</a>

  <p class="quote abs" style="top:774px">Praesent et turpis dui. Phasellus porta est vel tortor interdum nec laoreet turpis gravida. Ut ultrices nisl sit amet leo auctor eu suscipit magna vestibulum.&nbsp; - Dana Mercer</p>
  <p class="quote abs" style="top:852px">Praesent et turpis dui. Phasellus porta est vel tortor interdum nec laoreet turpis gravida. Ut ultrices nisl sit amet leo auctor eu suscipit magna vestibulum.&nbsp; - Dana Mercer</p>

  <div class="icon-box abs" role="img" aria-label="Illustration of a contact card icon" style="left:210px;top:940px;background:linear-gradient(#d9b35a,#8c6418)"></div>
  <h2 class="section-title abs" style="left:258px;top:940px">Contact Us</h2>
  <p class="contact-intro abs">Send us quick email with any questions or concerns you may have about your potential case</p>

  <span class="field-label abs" style="left:209px;top:1045px">Name</span>
  <span class="field abs" style="left:249px;top:1040px;width:165px"></span>
  <span class="field-label abs" style="left:209px;top:1072px">Phone</span>
  <span class="field abs" style="left:249px;top:1068px;width:165px"></span>
  <span class="field-label abs" style="left:209px;top:1099px">Email</span>
  <span class="field abs" style="left:249px;top:1095px;width:165px"></span>
  <span class="field-label abs" style="left:437px;top:1040px">Tell us about your case</span>
  <span class="field abs" style="left:432px;top:1060px;width:174px;height:37px"></span>
  <a class="btn submit abs">Submit</a>

  <!-- right sidebar -->
  <h3 class="side-title abs" style="top:433px">Video Center</h3>
  <div class="side-icon abs" role="img" aria-label="Video player icon" style="top:471px;background:linear-gradient(#444,#111);border:2px solid #bbb"></div>
  <p class="side-text abs" style="top:470px">Need more information ?<br>Learn more about your case from our informative videos</p>

  <h3 class="side-title abs" style="top:566px">Click to Call</h3>
  <div class="side-icon abs" role="img" aria-label="Mobile phone icon" style="top:602px;left:666px;width:38px;height:60px;border-radius:6px;background:linear-gradient(#333,#0a0a0a)"></div>
  <p class="side-text abs" style="top:603px">Need more information ?<br>Learn more about your case from our informative videos</p>

  <h3 class="side-title abs" style="top:710px">Click for Awards</h3>
  <div class="side-icon abs" role="img" aria-label="Trophy illustration" style="top:748px;border-radius:20px 20px 6px 6px;background:linear-gradient(#f0e6c8,#7a5a20)"></div>
  <p class="side-text abs" style="top:747px">Need more information ?<br>Learn more about your case from our informative videos</p>

  <h3 class="side-title abs" style="top:842px">Click for Testimonial</h3>
  <div class="side-icon abs" role="img" aria-label="Illustration of a testimonial note" style="top:878px;height:56px;background:#fbfaf5;border:1px solid #ddd"></div>
  <p class="side-text abs" style="top:879px">Need more information ?<br>Learn more about your case from our informative videos</p>

  <h3 class="side-title abs" style="top:973px">Case Evaluation</h3>
  <div class="side-icon abs" role="img" aria-label="Illustration of a document with pen" style="top:1010px;background:linear-gradient(135deg,#fafafa,#cfcfcf);transform:rotate(-10deg)"></div>
  <p class="side-text abs" style="top:1010px">Need more information ?<br>Learn more about your case from our informative videos</p>

  <!-- footer -->
  <footer class="footer abs"></footer>
  <div class="footer-brand abs"><i></i>Halvorsen Law</div>
  <div class="footer-links abs">Home<span>~</span>Meet Our Attorney<span>~</span>FAQ<span>~</span>Why Halvorsen<span>~</span>Contact Us</div>
  <div class="copyright abs">© 2012 All Rights Reserved.</div>
  <div class="pay abs" style="left:672px;top:1145px;width:40px">Paycard</div>
  <div class="pay abs" style="left:731px;top:1145px;width:40px">Duocard</div>
  <div class="pay abs" style="left:786px;top:1145px;width:40px">Amcard</div>
  <div class="pay seal abs" style="left:697px;top:1180px;width:64px">SecureSeal</div>
  <div class="pay seal abs" style="left:773px;top:1180px;width:50px">SafeScan</div>

</div>
</body>
</html>
```